CareVantRx business cards

We need a business card design that we could customize as needed for employees. We will need space for Name, Title, 1-2 phone numbers and email address.

We are a Pharmacy Benefits Management (PBM) company for hospice agencies and beginning a nationwide expansion. Attached is a vector file of our logo.

Cards can be single or double sided.

Industry/Entity Type

Business

```html
<!DOCTYPE html>
<html lang="en">
<head>
<meta charset="utf-8">
<title>CareVantRx Business Cards</title>
<link rel="stylesheet" href="https://fonts.googleapis.com/css2?family=Questrial&family=Open+Sans:wght@400;600;700&display=swap">
<style>
  :root {
    --brand-blue: #336a91;
    --brand-blue-dark: #2b5f86;
    --brand-green: #7f9c3f;
    --card-white: #ffffff;
    --text-dark: #3a3a3a;
    --divider: #c9c9c9;
    --backdrop: #e6e7e9;
  }
  * { margin: 0; padding: 0; box-sizing: border-box; }
  html, body {
    width: 1200px;
    height: 900px;
    overflow: hidden;
    background: var(--backdrop);
  }
  .canvas {
    position: relative;
    width: 1200px;
    height: 900px;
  }
  .card {
    position: absolute;
    left: 320px;
    width: 560px;
    height: 320px;
    overflow: hidden;
    box-shadow: 0 6px 18px rgba(0,0,0,0.18);
  }
  /* Front side */
  .card-front {
    top: 100px;
    background: var(--card-white);
  }
  .front-swoosh {
    position: absolute;
    left: 0;
    top: 0;
    width: 560px;
    height: 320px;
  }
  .front-wordmark {
    position: absolute;
    left: 52px;
    top: 118px;
    font-family: "Questrial", sans-serif;
    font-size: 38px;
    color: var(--brand-blue);
    letter-spacing: -0.5px;
  }
  .front-divider {
    position: absolute;
    left: 300px;
    top: 98px;
    width: 1px;
    height: 92px;
    background: var(--divider);
  }
  .contact-block {
    position: absolute;
    left: 322px;
    top: 102px;
    font-family: "Open Sans", sans-serif;
  }
  .person-name {
    font-size: 18px;
    font-weight: 700;
    color: var(--brand-blue);
    line-height: 1.1;
  }
  .person-title {
    font-size: 13px;
    color: var(--brand-green);
    margin-bottom: 12px;
  }
  .contact-list {
    list-style: none;
  }
  .contact-item {
    display: flex;
    align-items: center;
    gap: 8px;
    font-size: 13px;
    color: var(--text-dark);
    line-height: 20px;
  }
  .contact-icon {
    width: 11px;
    height: 11px;
    flex: none;
  }
  /* Back side */
  .card-back {
    top: 480px;
    background: var(--brand-blue);
    display: flex;
    align-items: center;
    justify-content: center;
  }
  .back-wordmark {
    font-family: "Questrial", sans-serif;
    font-size: 46px;
    color: var(--card-white);
    letter-spacing: -0.5px;
  }
</style>
</head>
<body>
<main class="canvas">

  <section class="card card-front" aria-label="Business card front">
    <svg class="front-swoosh" viewBox="0 0 560 320" aria-hidden="true">
      <path d="M0 262 C170 276 360 298 560 318" fill="none" stroke="var(--brand-green)" stroke-width="3"/>
      <path d="M0 272 C170 286 360 306 560 326 L560 320 L0 320 Z" fill="var(--brand-blue)"/>
    </svg>

    <div class="front-wordmark">CareVantRx</div>
    <div class="front-divider"></div>

    <div class="contact-block">
      <p class="person-name">Dana Whitfield</p>
      <p class="person-title">CareVantRx</p>
      <ul class="contact-list">
        <li class="contact-item">
          <svg class="contact-icon" viewBox="0 0 12 12" aria-hidden="true">
            <path d="M2.5 1 L4.5 1 L5.3 3.6 L4 4.6 C4.7 6 6 7.3 7.4 8 L8.4 6.7 L11 7.5 L11 9.5 C11 10.3 10.3 11 9.5 11 C5 11 1 7 1 2.5 C1 1.7 1.7 1 2.5 1 Z" fill="var(--brand-green)"/>
          </svg>
          <span>(+00) 000 000 000</span>
        </li>
        <li class="contact-item">
          <svg class="contact-icon" viewBox="0 0 12 12" aria-hidden="true">
            <rect x="3" y="0.5" width="6" height="11" rx="1" fill="none" stroke="var(--brand-green)" stroke-width="1.2"/>
            <circle cx="6" cy="9.5" r="0.8" fill="var(--brand-green)"/>
          </svg>
          <span>(+00) 000 000 000</span>
        </li>
        <li class="contact-item">
          <svg class="contact-icon" viewBox="0 0 12 12" aria-hidden="true">
            <rect x="0.5" y="2" width="11" height="8" fill="var(--brand-green)"/>
            <path d="M0.5 2 L6 6.5 L11.5 2" fill="none" stroke="var(--card-white)" stroke-width="1"/>
          </svg>
          <span>carevantrx@teamcontact.com</span>
        </li>
      </ul>
    </div>
  </section>

  <section class="card card-back" aria-label="Business card back">
    <div class="back-wordmark">CareVantRx</div>
  </section>

</main>
</body>
</html>
```